We are a new towing and recovery company starting out in Tallow Creek, ST. We do not want anything generic, we are looking to stand out. we will be doing towing for motorcycles to straight trucks we will have a rollback a 16-ton wrecker and a service vehicle with a wheel lift attached to tow small sized vehicles. We will also be doing roadside services which include lock-out, fuel delivery, jumpstarts, tire changes, and minor auto repair. we will be providing a quality and fast service also customer service will be one of main focuses.

Contact Information for Business Card

Brindle Towing and Recovery, Gus Lindqvist, Owner, 48213 S. Orrin Road, Tallow Creek, ST 00000 555-562-9147 Phone 555-562-9288 Fax www.brindletowingandrecovery.example

```html
<!DOCTYPE html>
<html lang="en">
<head>
<meta charset="utf-8">
<title>Brindle Towing and Recovery — Business Card</title>
<link rel="stylesheet" href="https://fonts.googleapis.com/css2?family=Oswald:wght@600&family=Open+Sans:wght@400;600&display=swap">
<style>
  :root {
    --backdrop: #d8d5d1;
    --paper: #eeedeb;
    --paper-edge: #e2e0dd;
    --accent: #f26a21;
    --ink: #4a4a4a;
    --ink-soft: #6b6b6b;
    --icon: #5a5a5a;
  }
  html, body {
    margin: 0;
    width: 1200px;
    height: 1000px;
    overflow: hidden;
    background: var(--backdrop);
  }
  .card {
    position: absolute;
    left: 100px;
    top: 214px;
    width: 1000px;
    height: 572px;
    background: radial-gradient(ellipse at 40% 40%, var(--paper) 0%, var(--paper) 55%, var(--paper-edge) 100%);
    box-shadow: 0 8px 24px rgba(0,0,0,.18);
    overflow: hidden;
    font-family: "Open Sans", Arial, sans-serif;
  }
  .truck-watermark {
    position: absolute;
    left: 330px;
    top: 135px;
    width: 430px;
    height: 310px;
    border-radius: 24px;
    background: linear-gradient(160deg, #e9e3b8 0%, #ddd8c6 60%, #d6d4cf 100%);
    opacity: .45;
  }
  .truck-illustration {
    position: absolute;
    border-radius: 18px;
  }
  .truck-illustration--wrecker {
    left: 785px;
    top: 28px;
    width: 185px;
    height: 140px;
    background: linear-gradient(135deg, #8a8f96 0%, #d94a3c 40%, #f4f1ee 70%, #9aa2ab 100%);
  }
  .truck-illustration--wheel-lift {
    left: 40px;
    top: 180px;
    width: 235px;
    height: 140px;
    background: linear-gradient(110deg, #3c63b4 0%, #6e8fd0 35%, #f3f3f3 65%, #b8bcc4 100%);
  }
  .brand-title {
    position: absolute;
    left: 215px;
    top: 60px;
    margin: 0;
    padding-bottom: 4px;
    font-family: "Oswald", "Arial Narrow", sans-serif;
    font-weight: 600;
    font-size: 40px;
    letter-spacing: .5px;
    color: var(--accent);
    border-bottom: 3px solid var(--accent);
    text-transform: uppercase;
  }
  .person {
    position: absolute;
    left: 420px;
    top: 205px;
    text-align: center;
  }
  .person__name {
    margin: 0;
    font-weight: 600;
    font-size: 36px;
    color: var(--accent);
    letter-spacing: .5px;
  }
  .person__role {
    margin: 0;
    font-size: 22px;
    color: var(--ink-soft);
    letter-spacing: 1px;
  }
  .contact {
    position: absolute;
    margin: 0;
    padding: 0;
    list-style: none;
    font-size: 17px;
    color: var(--ink);
  }
  .contact li {
    display: flex;
    align-items: center;
    gap: 12px;
    margin-bottom: 12px;
  }
  .contact svg { width: 22px; height: 22px; flex: none; }
  .contact--phones { left: 680px; top: 318px; }
  .contact--location { left: 240px; top: 440px; }
</style>
</head>
<body>
  <main class="card">
    <div class="truck-watermark" role="img" aria-label="Faint illustration of a flatbed rollback truck in the background"></div>
    <div class="truck-illustration truck-illustration--wheel-lift" role="img" aria-label="Cartoon illustration of a blue and white wheel-lift tow truck"></div>
    <div class="truck-illustration truck-illustration--wrecker" role="img" aria-label="Cartoon illustration of a red and white heavy wrecker"></div>

    <h1 class="brand-title">Brindle Towing and Recovery</h1>

    <div class="person">
      <p class="person__name">Gus Lindqvist</p>
      <p class="person__role">Owner</p>
    </div>

    <ul class="contact contact--phones">
      <li>
        <svg viewBox="0 0 24 24" aria-hidden="true"><circle cx="12" cy="12" r="12" fill="var(--icon)"/><path d="M8.5 6.5l2 2-1.2 1.6a7 7 0 0 0 4.6 4.6l1.6-1.2 2 2-1.3 1.8C11.5 17 7 12.5 6.7 7.8z" fill="#fff"/></svg>
        <span>00000 555-562-9147</span>
      </li>
      <li>
        <svg viewBox="0 0 24 24" aria-hidden="true"><circle cx="12" cy="12" r="12" fill="var(--icon)"/><rect x="8" y="6" width="8" height="4" fill="#fff"/><rect x="6" y="10" width="12" height="5" rx="1" fill="#fff"/><rect x="8" y="14" width="8" height="4" fill="#fff" stroke="var(--icon)" stroke-width="1"/></svg>
        <span>555-562-9288</span>
      </li>
    </ul>

    <ul class="contact contact--location">
      <li>
        <svg viewBox="0 0 24 24" aria-hidden="true"><circle cx="12" cy="12" r="12" fill="var(--icon)"/><path d="M12 6l6 5.5h-2V17h-3v-3.5h-2V17H8v-5.5H6z" fill="#fff"/></svg>
        <span>48213 S. Orrin Road, Tallow Creek, ST</span>
      </li>
      <li>
        <svg viewBox="0 0 24 24" aria-hidden="true"><circle cx="12" cy="12" r="12" fill="var(--icon)"/><circle cx="12" cy="12" r="5.5" fill="none" stroke="#fff" stroke-width="1.4"/><path d="M6.5 12h11M12 6.5c-2.5 3-2.5 8 0 11M12 6.5c2.5 3 2.5 8 0 11" fill="none" stroke="#fff" stroke-width="1.2"/></svg>
        <span>www.brindletowingandrecovery.example</span>
      </li>
    </ul>
  </main>
</body>
</html>
```